Flyer for the Radiant Harvest Worship Day 2020

I am looking to create a flyer for a one day prayer retreat our church is organizing.
This flyer will be posted on social media, websites and will also be printed so it can be mailed to people.
I am looking for something professional, with good use of our logo and band colors (logo colors).
I am counting on the designer's skill, creativity, art and knowledge of media communication to produce a flyer that will effectively and quickly convey the message we are trying to spread.
CONTENT OF THE FLYER:
Event title: Radiant Harvest Worship Day
Date: Tuesday July 2nd, 2020
Time: 11:00AM - 7:00PM
Belmora Hotel, 4876 Willowmere Street, Portland, Maine 04987 (Room: Evergrove)
Event Key words to highlight what the event is about: Prayer, Sharing the Word, Panel discussion, prophecy, Impartation.
Key phrases:
A one day prayer retreat.
Jesus Chris is Lord
Contact info:
www.toluvek.org
Phone: 207 555 0183
Email: contact@brightmeadowfold.org

```html
<!DOCTYPE html>
<html lang="en">
<head>
<meta charset="utf-8">
<title>Radiant Harvest Worship Day 2020</title>
<link rel="stylesheet" href="https://fonts.googleapis.com/css2?family=Archivo+Black&family=Great+Vibes&family=Cormorant+Garamond:wght@600;700&family=Roboto:wght@400;700;900&display=swap">
<style>
:root{
  --navy:#133a63;
  --orange:#f39322;
  --white:#ffffff;
  --page:#ffffff;
  --ink:#111111;
  --photo-top:#a6c5df;
  --photo-mid:#7ea5c2;
  --photo-low:#e4ddd2;
}
*{margin:0;padding:0;box-sizing:border-box}
html,body{width:1200px;height:1200px;overflow:hidden;background:var(--page)}
.flyer{
  position:absolute;left:202px;top:84px;width:796px;height:1032px;
  background:var(--white);overflow:hidden;
}
.hero-photo{
  position:absolute;left:0;top:0;width:796px;height:790px;
  background:linear-gradient(to bottom,
    var(--photo-top) 0%, var(--photo-mid) 55%, var(--photo-low) 82%, var(--white) 100%);
}
.brand{
  position:absolute;left:0;right:0;top:58px;
  display:flex;justify-content:center;align-items:center;gap:12px;
  font-family:"Cormorant Garamond",serif;font-weight:700;
  font-size:46px;letter-spacing:2px;color:var(--navy);
}
.brand-dot{width:16px;height:16px;border-radius:50%;background:var(--orange)}
.title{position:absolute;left:0;right:0;text-align:center;font-family:"Archivo Black",sans-serif;line-height:1;white-space:nowrap}
.title-top{top:142px;font-size:64px;color:var(--navy)}
.title-main{top:206px;font-size:86px;color:var(--orange);letter-spacing:1px}
.tagline{
  position:absolute;left:0;right:0;top:304px;text-align:center;
  font-family:"Roboto",sans-serif;font-size:32px;letter-spacing:1.5px;color:var(--white);
}
.motto{
  position:absolute;left:0;right:0;top:574px;text-align:center;
  font-family:"Great Vibes",cursive;font-size:56px;color:var(--white);
}
.details{
  position:absolute;left:62px;top:712px;width:680px;height:78px;
  display:flex;align-items:center;color:var(--navy);font-family:"Roboto",sans-serif;
}
.day-number{font-family:"Archivo Black",sans-serif;font-size:74px;line-height:1}
.month-year{margin-left:12px;font-family:"Archivo Black",sans-serif;font-size:31px;line-height:1.05}
.divider{width:2px;height:74px;background:var(--orange);margin:0 16px}
.venue{width:196px;text-align:center;font-weight:700;font-size:15px;line-height:1.25}
.weekday{font-family:"Archivo Black",sans-serif;line-height:1.05;font-size:36px}
.weekday span{display:block;font-size:31px}
.topics{
  position:absolute;left:62px;top:814px;width:672px;height:124px;
  border:3px solid var(--orange);border-radius:16px;
}
.topic{
  position:absolute;font-family:"Cormorant Garamond",serif;font-weight:700;
  font-variant:small-caps;font-size:27px;color:var(--ink);line-height:1;
}
.topic::before{content:"";display:inline-block;width:11px;height:11px;background:var(--ink);transform:rotate(45deg);margin-right:10px;vertical-align:3px}
.contacts{
  position:absolute;left:34px;top:952px;
  font-family:"Cormorant Garamond",serif;font-weight:700;font-variant:small-caps;
  font-size:19px;color:var(--ink);line-height:30px;
}
.contacts div{display:flex;align-items:center;gap:12px}
.phone-pill{
  position:absolute;left:384px;top:958px;width:386px;height:52px;
  background:var(--orange);border-radius:12px;
  display:flex;align-items:center;
}
.phone-badge{
  width:56px;height:56px;border-radius:50%;background:var(--white);
  border:3px solid var(--orange);margin-left:-2px;
  display:flex;align-items:center;justify-content:center;
}
.phone-number{
  margin-left:34px;font-family:"Cormorant Garamond",serif;font-weight:600;
  font-size:42px;color:var(--white);letter-spacing:1.5px;
  font-variant-numeric:lining-nums;font-feature-settings:"lnum" 1;
}
</style>
</head>
<body>
<main class="flyer">
  <div class="hero-photo" role="img" aria-label="Photo of a man kneeling in prayer on a sandy beach by the sea, open Bible faintly in the sky"></div>

  <div class="brand"><span class="brand-dot"></span>VELANOR</div>

  <h1 class="title title-top">RADIANT HARVEST</h1>
  <h2 class="title title-main">WORSHIP DAY</h2>
  <p class="tagline">A one day prayer retreat.</p>
  <p class="motto">Jesus Christ is Lord</p>

  <section class="details">
    <span class="day-number">02</span>
    <span class="month-year">JULY<br>2020</span>
    <span class="divider"></span>
    <span class="venue">EVERGROVE ROOM<br>Belmora Hotel,<br>4876 Willowmere Street,<br>Portland, Maine 04987</span>
    <span class="divider"></span>
    <span class="weekday">TUESDAY<span>11AM–7PM</span></span>
  </section>

  <section class="topics">
    <span class="topic" style="left:42px;top:16px">Prayer</span>
    <span class="topic" style="left:42px;top:50px">Sharing the Word</span>
    <span class="topic" style="left:42px;top:84px">Panel discussion</span>
    <span class="topic" style="left:352px;top:16px">Prophecy</span>
    <span class="topic" style="left:352px;top:50px">Impartation</span>
  </section>

  <section class="contacts">
    <div>
      <svg width="20" height="14" viewBox="0 0 20 14"><rect width="20" height="14" rx="1" fill="#111"/><path d="M1 1l9 7 9-7" stroke="#fff" stroke-width="1.6" fill="none"/></svg>
      contact@brightmeadowfold.org
    </div>
    <div>
      <svg width="20" height="20" viewBox="0 0 20 20" fill="none" stroke="#111" stroke-width="1.6"><circle cx="10" cy="10" r="8.5"/><ellipse cx="10" cy="10" rx="3.8" ry="8.5"/><path d="M1.5 10h17M3 5.5h14M3 14.5h14"/></svg>
      www.toluvek.org
    </div>
  </section>

  <div class="phone-pill">
    <span class="phone-badge">
      <svg width="28" height="28" viewBox="0 0 24 24"><path fill="#f39322" d="M6.6 10.8a15.1 15.1 0 0 0 6.6 6.6l2.2-2.2a1 1 0 0 1 1-.25 11.4 11.4 0 0 0 3.6.57 1 1 0 0 1 1 1V20a1 1 0 0 1-1 1A17 17 0 0 1 3 4a1 1 0 0 1 1-1h3.5a1 1 0 0 1 1 1c0 1.25.2 2.450.57 3.57a1 1 0 0 1-.25 1z"/></svg>
    </span>
    <span class="phone-number">207 555 0183</span>
  </div>
</main>
</body>
</html>
```